Sassy, natural personal lubricant knows that it is not always about the packaging

An opportunity exists to create packaging for the world's first Macadamia Oil personal lubricant - Vorrabee Silk. Unlike any other personal lubricants, this product is created from pure macadamia nut oil. The fatty acids naturally occurring in Macadamia oil are highly anti-inflammatory and are the closest in composition to human skin lipids. Using Vorrabee Silk in such a vulnerable part of our bodies is the safest and gentlest way to enhance sexual enjoyment while moisturizing and adding lubrication. Vorrabee Silk is completely free of the parabens, glycerins, fragrances, hormones, silicones and petroleum products known to irritate the delicate vaginal wall.

Design tone for Vorrabee Silk:
- intelligent, but not condescending or patronizing
- elegant and dignified but not prudish
- clean, natural, uninhibited

Design specs:
- See attached file for packaging specs

Colors:
- refer to www.vorrabee-example.com to see other products in the range. This is a guide only. Use of those colors is not mandatory.

Ingredients:

100% Macadamia Oil

Additional features:

- edible
- vegan
- gluten-free
- low allergen
- naturally anti-microbial and anti-inflammatory

See http://plumfernlab-example.com/benefits-of-macadamia-nut-oil-in-skin-care/ for a list of the benefits of macadamia oil.

Target Market(s)

Our target market are the early adopters within the baby boomer set. Their age is a badge of honor, they are comfortable in their own skin and as sensual and fun-loving as ever. They are in their prime - still cool, still curious, still a little crazy. They are open to new possibilities, just as they have been at every age and stage. They still have plenty to do and plenty to enjoy. Being pre-menopausal or menopausal, natural lubrication may be diminishing. Vorrabee Silk is the completely natural way to bring back the pleasure in sex.

Requirements
Must have
• Brandname: Vorrabee Silk

Container Packaging specs: http://www.gravelpackco-example.com/images/art/7845K16-K-OAK-PRESSED.PDF
Dispenser: http://www.gravelpackco-example.com/lotion-dispenser-pumps/p/kMQ730R/
Should not have
• No post-coital pictures
No people
Nothing phallic

```html
<!DOCTYPE html>
<html lang="en">
<head>
<meta charset="utf-8">
<title>Vorrabee Silk – Macadamia Oil Label</title>
<link rel="stylesheet" href="https://fonts.googleapis.com/css2?family=Oswald:wght@400;500;600&display=swap">
<style>
  :root {
    --backdrop: #e6e4e1;
    --bark: #5b3a21;
    --bark-dark: #3b2312;
    --bark-light: #7a5230;
    --leaf: #a9c83a;
    --leaf-light: #c3dc55;
    --lime-rule: #c6e03a;
    --oval: #3d1d0e;
    --cream: #f4ecd2;
    --ink-light: #fbfbf3;
    --nut: #a8743f;
  }
  html, body {
    margin: 0;
    padding: 0;
    width: 1200px;
    height: 779px;
    overflow: hidden;
    background: var(--backdrop);
  }
  .label {
    display: block;
    width: 1200px;
    height: 779px;
  }
  .label-text {
    font-family: "Oswald", "Arial Narrow", sans-serif;
  }
  .brand-name {
    font-size: 40px;
    font-weight: 500;
    fill: var(--bark-dark);
    letter-spacing: 1px;
  }
  .product-title {
    font-size: 60px;
    font-weight: 600;
    fill: var(--cream);
    letter-spacing: 1px;
  }
  .ingredient-line {
    font-size: 24px;
    font-weight: 500;
    fill: var(--ink-light);
  }
  .feature-list {
    font-size: 15px;
    font-weight: 400;
    fill: var(--ink-light);
    letter-spacing: 0.5px;
  }
</style>
</head>
<body>
<svg class="label" viewBox="0 0 1200 779" xmlns="http://www.w3.org/2000/svg">
  <defs>
    <linearGradient id="barkShade" x1="0" y1="0" x2="1" y2="0">
      <stop offset="0" stop-color="var(--bark-dark)"/>
      <stop offset="0.5" stop-color="var(--bark-light)"/>
      <stop offset="1" stop-color="var(--bark-dark)"/>
    </linearGradient>
    <linearGradient id="leafShade" x1="0" y1="0" x2="0" y2="1">
      <stop offset="0" stop-color="var(--leaf-light)"/>
      <stop offset="1" stop-color="var(--leaf)"/>
    </linearGradient>
    <radialGradient id="nutShade" cx="0.5" cy="0.5" r="0.6">
      <stop offset="0" stop-color="#e6cf9a"/>
      <stop offset="0.6" stop-color="var(--nut)"/>
      <stop offset="1" stop-color="var(--leaf)" stop-opacity="0"/>
    </radialGradient>
  </defs>

  <!-- label body -->
  <rect class="label-body" x="170" y="60" width="860" height="660" fill="url(#barkShade)"/>

  <!-- side panel patterns -->
  <rect class="side-pattern" x="170" y="60" width="285" height="660" fill="var(--bark)" opacity="0.35"
        role="img" aria-label="Ornamental swirl pattern in brown tones"/>
  <rect class="side-pattern" x="745" y="60" width="285" height="660" fill="var(--bark)" opacity="0.35"
        role="img" aria-label="Ornamental swirl pattern in brown tones"/>

  <!-- central band -->
  <rect class="centre-band" x="455" y="60" width="290" height="660" fill="url(#leafShade)"/>

  <!-- brand -->
  <circle class="brand-dot" cx="600" cy="165" r="50" fill="var(--bark-dark)"/>
  <text class="label-text brand-name" x="600" y="275" text-anchor="middle">Vorrabee Silk</text>

  <!-- product title oval -->
  <ellipse class="title-oval" cx="600" cy="400" rx="232" ry="86" fill="var(--oval)" stroke="var(--lime-rule)" stroke-width="3"/>
  <text class="label-text product-title" x="600" y="420" text-anchor="middle">MACADAMIA OIL</text>

  <!-- nut photo area -->
  <ellipse class="nut-photo" cx="600" cy="505" rx="108" ry="48" fill="url(#nutShade)"
           role="img" aria-label="Photograph of whole and cracked macadamia nuts"/>

  <!-- ingredients and features -->
  <text class="label-text ingredient-line" x="600" y="597" text-anchor="middle">100% MACADAMIA OIL</text>
  <text class="label-text feature-list" text-anchor="middle">
    <tspan x="600" y="627">EDIBLE</tspan>
    <tspan x="600" y="643">VEGAN</tspan>
    <tspan x="600" y="659">GLUTEN-FREE</tspan>
    <tspan x="600" y="675">LOW ALLERGEN</tspan>
    <tspan x="600" y="691">NATURALLY ANTI-MICROBIAL</tspan>
    <tspan x="600" y="707">ANTI-INFLAMMATORY</tspan>
  </text>
</svg>
</body>
</html>
```